Non-Profit Needs Plastic Recycling Infographic

We need a modern infographic to help illustrate international recycling rates for expanded polystyrene plastic. Include the information below and use the attached PowerPoint as an example for your design – the PowerPoint is just to illustrate the information; you do not need to follow it completely.

We have also included our updated color guide.

Please fit the following information into the infographic:
• The one item that is necessary is the global map – the "Global EPS Packaging Recycling" header is not required
• Do NOT include any "chasing arrows" recycling symbols
• the "34 Countries" should read "34 Countries with a Confirmed Recycling Rate"
• "34 Countries" should be an information block along with the "21 Countries"
• The "32 Countries" and "62 Countries" should be included in the graph image – we have given a pie graph as an example, though it can be another graph
• "Leading EPS Recyclate Sources" should have the following four blocks associated with it: Automotive, Seafood & Fishers, Furniture, and Appliances; use attached photos for blocks
• The lorem ipsum vertical information blocks should include 3 columns:
#1: "Developing Countries Recycle EPS" – include country outline of Guatemala; include the text "EPS manufacturing is working with government in Guatemala. Where an EPS molder exists is the easiest way to initiate EPS recycling. Work with the EPS manufacturing sector can promote quick startup of B2B recycling programs."
#2: "Small Islands Recycle EPS" – include country outline of Dominican Republic; include the text "An EPS recycling program in the Dominican Republic highlighted the need for new polystyrene recycling technologies. Through their work with machinery specialists, they were able to identify a solution that then spread to other nations."
#3: "Local Communities Recycle EPS" – include country outline of China; include text "EPS startups can lead to successful recycling collection programs. Tulvenka Neighborhood Office in Xiamen City, China, was already receiving polystyrene for recycling when they were able to procure a densifier. Since installation, the program has spread to five machines located across the city."
• Under the "Varnholt Waste Stewardship Accord" statement, include the following: "Criteria could be tailored to specific applications, allowing for country-specific flexibility. This approach would also help to develop standards on a material basis and allow countries to focus on scientific research and assess availability of recycling programs."

Sans Serif

• 1. Global EPS Recycling Map (see attached documents), 2. Infographic should be vertical in design, NOT horizontal
• Chasing Arrows Recycling Symbols

```html
<!DOCTYPE html>
<html lang="en">
<head>
<meta charset="utf-8">
<title>Global EPS Packaging Recycling</title>
<link href="https://fonts.googleapis.com/css2?family=Bebas+Neue&family=Poppins:wght@700;800&family=Rubik:wght@400;500&display=swap" rel="stylesheet">
<style>
:root{
  --navy:#162a4d;
  --coral:#ef8450;
  --gold:#f4ab2f;
  --sand:#fdd98a;
  --text:#2b2b33;
  --muted:#55565e;
  --card:#ffffff;
  --bg:#ffffff;
  --label:#ececee;
}
*{box-sizing:border-box;margin:0;padding:0}
html,body{width:1200px;height:2369px;overflow:hidden;background:var(--bg)}
body{position:relative;font-family:"Rubik",sans-serif;color:var(--text)}
.abs{position:absolute}
.title-band{left:30px;top:28px;width:1143px;height:138px;background:var(--navy);display:flex;align-items:center;justify-content:center}
.title-band h1{font-family:"Bebas Neue",sans-serif;font-weight:400;color:#fff;font-size:104px;letter-spacing:1px;line-height:1;padding-top:8px}
.shadow{box-shadow:0 3px 10px rgba(0,0,0,.13)}
.map{left:30px;top:190px;width:858px;height:403px;background:#fff}
.map-fill{position:absolute;left:60px;top:30px;width:760px;height:350px;border-radius:40% 45% 38% 42%;background:radial-gradient(ellipse at 30% 40%,#f6a623 0 22%,transparent 40%),radial-gradient(ellipse at 80% 80%,#f6a623 0 12%,transparent 25%),linear-gradient(135deg,var(--sand),#f8c45e)}
.stat-box{left:911px;width:262px;background:#fff;padding:14px 0 0 48px}
.stat-box::before{content:"";position:absolute;left:0;top:0;bottom:0;width:24px;background:var(--coral)}
.stat-box .num{font-family:"Poppins",sans-serif;font-weight:800;color:var(--coral);font-size:86px;line-height:.95}
.stat-box p{font-size:24px;line-height:31px;color:var(--text)}
.stat-box b{font-weight:500}
.pie-row{left:30px;top:642px;width:1143px;height:197px;background:#fff}
.pie-row .bar-l,.pie-row .bar-r{position:absolute;top:0;bottom:0;width:24px;background:var(--navy)}
.pie-row .bar-l{left:12px}.pie-row .bar-r{right:12px}
.pie-stat{position:absolute;top:34px}
.pie-stat .num{font-family:"Poppins",sans-serif;font-weight:800;color:var(--navy);font-size:86px;line-height:.95}
.pie-stat p{font-size:24px;line-height:31px}
.pie-chart{left:462px;top:601px;width:276px;height:276px}
.legend{top:857px;font-size:26px;display:flex;align-items:center;gap:12px;color:var(--text)}
.legend i{display:block;width:28px;height:28px}
.cat{width:240px;top:923px;height:245px;background:#fff}
.cat .tab{position:absolute;left:0;top:0;width:100%;height:24px;background:var(--gold)}
.cat .label{position:absolute;left:-14px;top:36px;width:270px;height:42px;background:var(--label);box-shadow:0 3px 6px rgba(0,0,0,.12);font-family:"Poppins",sans-serif;font-weight:700;font-size:25px;color:#3a3b40;display:flex;align-items:center;justify-content:center}
.cat .photo{position:absolute;left:22px;top:102px;width:196px;height:130px;border-radius:6px}
.summary{left:43px;top:1190px;width:1118px;height:162px;background:var(--navy);color:#fff;font-size:25.5px;line-height:32px;padding:16px 20px 0 22px}
.story{left:43px;width:1114px;height:225px}
.story svg.frame{position:absolute;left:0;top:0}
.story .outline{position:absolute;left:34px;top:50px;width:136px;height:136px;background:#fff;box-shadow:0 2px 8px rgba(0,0,0,.15)}
.story .outline div{position:absolute;left:10px;top:10px;width:116px;height:116px;background:linear-gradient(#f6a623,#f4ab2f);border-radius:30% 40% 35% 45%}
.story h2{position:absolute;left:210px;top:20px;font-family:"Poppins",sans-serif;font-weight:800;font-size:34px;color:var(--navy);letter-spacing:-.3px}
.story p{position:absolute;left:210px;top:78px;width:830px;font-size:24px;line-height:29px;color:var(--muted)}
.accord{left:43px;top:2098px;width:1114px;height:82px;background:var(--coral);color:#fff;font-family:"Poppins",sans-serif;font-weight:700;font-size:22px;line-height:28px;padding:14px 22px}
.footnote{left:43px;top:2196px;width:1120px;font-size:21px;line-height:32px;color:var(--muted)}
</style>
</head>
<body>
<header class="abs title-band"><h1>GLOBAL EPS PACKAGING RECYCLING</h1></header>

<section class="abs map shadow">
  <div class="map-fill" role="img" aria-label="World map highlighting countries with EPS recycling in gold and orange tones"></div>
</section>

<div class="abs stat-box shadow" style="top:190px;height:187px">
  <div class="num">34</div>
  <p>Countries with a Confirmed Recycling Rate.</p>
</div>
<div class="abs stat-box shadow" style="top:407px;height:186px">
  <div class="num">21</div>
  <p>Countries have a recycling rate above <b>30%.</b></p>
</div>

<section class="abs pie-row shadow">
  <span class="bar-l"></span><span class="bar-r"></span>
  <div class="pie-stat" style="left:50px"><div class="num">62</div><p>Countries<br>recycle EPS.</p></div>
  <div class="pie-stat" style="left:900px"><div class="num">32%</div><p>Countries EPS<br>recycling.</p></div>
</section>

<svg class="abs pie-chart" viewBox="0 0 276 276" role="img" aria-label="Pie chart: 32% of countries recycle EPS">
  <defs>
    <radialGradient id="ring" cx="50%" cy="40%" r="60%"><stop offset="0" stop-color="#ffffff"/><stop offset="1" stop-color="#dcdcde"/></radialGradient>
  </defs>
  <circle cx="138" cy="138" r="136" fill="url(#ring)"/>
  <circle cx="138" cy="138" r="120" fill="#f7f7f8"/>
  <path d="M138 142 L138 40 A98 98 0 1 0 226 186 Z" fill="#162a4d"/>
  <path d="M150 134 L150 36 A98 98 0 0 1 232 178 Z" fill="#f4ab2f"/>
</svg>

<div class="abs legend" style="left:320px"><i style="background:var(--navy)"></i>No Recycling</div>
<div class="abs legend" style="left:706px"><i style="background:var(--gold)"></i>EPS Recycling</div>

<div class="abs cat shadow" style="left:46px"><span class="tab"></span><div class="label">Automotive</div><div class="photo" role="img" aria-label="Cross-section of a truck bumper with foam core" style="background:linear-gradient(160deg,#5d6670,#c9c3cf)"></div></div>
<div class="abs cat shadow" style="left:338px"><span class="tab"></span><div class="label" style="font-size:21px">Seafood &amp; Fishers</div><div class="photo" role="img" aria-label="Fresh fish on ice in a white foam cooler" style="background:linear-gradient(#aab4be,#eef0f2)"></div></div>
<div class="abs cat shadow" style="left:629px"><span class="tab"></span><div class="label">Furniture</div><div class="photo" role="img" aria-label="Washing machine with foam packaging" style="background:linear-gradient(120deg,#d6d8db,#9fa3a8)"></div></div>
<div class="abs cat shadow" style="left:920px"><span class="tab"></span><div class="label">Appliances</div><div class="photo" role="img" aria-label="White molded foam protective corner piece" style="background:linear-gradient(#f3f4f6,#c9cbcf)"></div></div>

<p class="abs summary">Automated manufacturing assembly parts packaging, cold chain shipping containers for fresh fish, bracing for furniture distribution &amp; packaging protection for appliances are key sources of EPS transport packaging being diverted from the landfill or otherwise mismanaged disposal practices</p>

<article class="abs story" style="top:1368px">
  <svg class="frame" width="1114" height="225" viewBox="0 0 1114 225"><polygon points="0,18 68,18 140,207 0,207" fill="#162a4d"/><polygon points="55,0 1114,0 1114,225 142,225" fill="#fff" style="filter:drop-shadow(0 3px 5px rgba(0,0,0,.14))"/><rect x="1064" y="0" width="22" height="225" fill="#f4ab2f"/></svg>
  <div class="outline"><div role="img" aria-label="Outline of Guatemala"></div></div>
  <h2>Developing Countries Recycle EPS</h2>
  <p>EPS manufacturing is working with government in Guatemala. Where an EPS molder exists is the easiest way to initiate EPS recycling. Work with the EPS manufacturing sector can promote quick startup of B2B recycling programs.</p>
</article>

<article class="abs story" style="top:1608px">
  <svg class="frame" width="1114" height="225" viewBox="0 0 1114 225"><polygon points="0,18 68,18 140,207 0,207" fill="#162a4d"/><polygon points="55,0 1114,0 1114,225 142,225" fill="#fff" style="filter:drop-shadow(0 3px 5px rgba(0,0,0,.14))"/><rect x="1064" y="0" width="22" height="225" fill="#f4ab2f"/></svg>
  <div class="outline"><div role="img" aria-label="Outline of the Dominican Republic"></div></div>
  <h2>Small Islands Recycle EPS</h2>
  <p>An EPS recycling program in the Dominican Republic highlighted the need for new polystyrene recycling technologies. Through their work with machinery specialists, they were able to identify a solution that then spread to other nations.</p>
</article>

<article class="abs story" style="top:1849px">
  <svg class="frame" width="1114" height="225" viewBox="0 0 1114 225"><polygon points="0,18 68,18 140,207 0,207" fill="#162a4d"/><polygon points="55,0 1114,0 1114,225 142,225" fill="#fff" style="filter:drop-shadow(0 3px 5px rgba(0,0,0,.14))"/><rect x="1064" y="0" width="22" height="225" fill="#f4ab2f"/></svg>
  <div class="outline"><div role="img" aria-label="Outline of China"></div></div>
  <h2>Local Communities Recycle EPS</h2>
  <p>EPS startups can lead to successful recycling collection programs. Tulvenka Neighborhood Office in Xiamen City, China, was already receiving polystyrene for recycling when they were able to procure a densifier. Since installation, the program has spread to five machines located across the city.</p>
</article>

<p class="abs accord">The Varnholt Waste Stewardship Accord Will Facilitate Improved Data Collection Through Mandatory Reporting Guidelines.</p>

<p class="abs footnote">Criteria could be tailored to specific applications, allowing for country-specific flexibility. This approach would also help to develop standards on a material basis and allow countries to focus on scientific research and assess availability of recycling programs.</p>
</body>
</html>
```